Tattoo Artist needs a personal business card designed

I am looking for a classy, clean, but antique feeling business card for myself that matches the theme and vibe of my tattoo shop. I would like to see a couple different options but we can go with an all black background, to start. I would like to see some western metallic lettering and deep/dark red accents. Maybe try adding a few with a mix of white fonts too. I would like to see the Shop's name and location which is Crane Voltage Ink, 4382 W. Delmora Ave. Tampa FL. 33617 Our tattoo shop has a western antique vibe, yet its classy and professional. We have a website you can see the color scheme and grab anymore information for designing this business card from: www.cranevoltageink.example - and if you want to add the website to the card. I would like my personal IG handle somewhere small with a unique and cleaner IG logo next to the name. My IG handle is: @tessadrillinkwork I am basically trying to look for multiple ideas/concepts that will match best with our website and sticker. (Which I will upload in the files) I would like it to be very clean, simple, classy, but have a western traditional tattooing feel to it. Like an antique stores business card. Add whatever information you think would be best, since I am not the professional graphic designer.
Shop Name: Crane Voltage Ink
Location: 4382 W Delmora Ave Tampa FL 33617
Website: www.cranevoltageink.example
Number: 813 555 0172
My Personal IG: @tessadrillinkwork

Thank you for taking your time to help me out with this project. Afterwards, I might need our studios website up for re-designing! So my end goal is to make everything intergraded with one another. I more likely need a logo too.

Target Market(s)

Professionals 35-55 years of age Male and Female
Firefighters, Military Service men and women

Contact Information for Business Card

All black background, with golden and red accents.
Traditional style, cowboy, western. Sharp, Clean, and Classy.

Requirements
Must have
• Shop Name - Crane Voltage Ink
• Shop Location - 4382 W Delmora Ave Tampa FL 33617
• My Name - Tessa Drill
• UNIQUE IG LOGO along with My Instagram - @tessadrillinkwork
• Number - 813 555 0172
Nice to have
• Gold metallic font
• Red accents
• Western Antique Oddity feel
• Might be nice to have the Website if it can work and fit in the space.

```html
<!DOCTYPE html>
<html lang="en">
<head>
<meta charset="utf-8">
<title>Crane Voltage Ink — Business Card</title>
<link rel="stylesheet" href="https://fonts.googleapis.com/css2?family=Cinzel:wght@400;600&family=Lato:wght@400&display=swap">
<style>
  :root {
    --backdrop: #e4e4e6;
    --card: #232323;
    --gold: #d4ab4a;
    --grey-text: #b4b4b4;
    --shadow: rgba(0, 0, 0, 0.28);
  }
  * { box-sizing: border-box; margin: 0; padding: 0; }
  html, body {
    width: 1200px;
    height: 900px;
    overflow: hidden;
    background: var(--backdrop);
  }
  .canvas { position: relative; width: 1200px; height: 900px; }
  .card {
    position: absolute;
    width: 640px;
    height: 366px;
    background: var(--card);
    border-radius: 26px;
    box-shadow: 0 14px 30px var(--shadow);
    overflow: hidden;
  }
  .card--front { left: 80px; top: 70px; display: flex; align-items: center; justify-content: center; }
  .card--back { left: 480px; top: 460px; }

  .shop-name {
    font-family: "Cinzel", serif;
    font-weight: 600;
    color: var(--gold);
    letter-spacing: 0.08em;
    white-space: nowrap;
  }
  .card--front .shop-name { font-size: 44px; }
  .card--back .shop-name { position: absolute; left: 42px; top: 92px; font-size: 34px; }

  .artist-name {
    position: absolute; left: 42px; top: 176px;
    font-family: "Cinzel", serif; font-weight: 600;
    font-size: 24px; letter-spacing: 0.06em; color: var(--gold);
  }
  .contact-list {
    position: absolute; left: 42px; top: 218px;
    list-style: none;
    font-family: "Lato", sans-serif; font-size: 17px; color: var(--grey-text);
    line-height: 26px;
  }
  .contact-item { display: flex; align-items: center; gap: 8px; color: #e6e6e6; }
  .contact-item svg { width: 15px; height: 15px; flex: none; }
  .address { margin-top: 12px; line-height: 24px; }

  .social-handle {
    position: absolute; right: 36px; top: 104px;
    display: flex; align-items: center; gap: 8px;
    font-family: "Lato", sans-serif; font-size: 16px; color: #e6e6e6;
  }
  .social-dot { width: 16px; height: 16px; border-radius: 50%; background: var(--gold); }
</style>
</head>
<body>
<main class="canvas">
  <section class="card card--front" aria-label="Card front">
    <h1 class="shop-name">Crane Voltage Ink</h1>
  </section>

  <section class="card card--back" aria-label="Card back">
    <p class="shop-name">Crane Voltage Ink</p>
    <p class="social-handle">@tessadrillinkwork <span class="social-dot"></span></p>
    <h2 class="artist-name">Tessa Drill</h2>
    <ul class="contact-list">
      <li class="contact-item">
        <svg viewBox="0 0 16 16" aria-hidden="true"><path fill="#d4ab4a" d="M3.5 1.5l2.6 2.8-1.4 1.8c.9 2 2.5 3.6 4.6 4.6l1.8-1.4 2.8 2.6-1.6 2.1C7.4 13.6 2.4 8.6 1.4 3.1z"/></svg>
        813 555 0172
      </li>
      <li class="contact-item">
        <svg viewBox="0 0 16 16" aria-hidden="true"><circle cx="8" cy="8" r="6.5" fill="none" stroke="#d4ab4a" stroke-width="1.6"/><path d="M1.5 8h13M8 1.5c-3 3.5-3 9.5 0 13M8 1.5c3 3.5 3 9.5 0 13" fill="none" stroke="#d4ab4a" stroke-width="1.2"/></svg>
        www.cranevoltageink.example
      </li>
      <li class="address">Crane Voltage Ink 4382<br>W Delmora Ave Tampa FL 33617</li>
    </ul>
  </section>
</main>
</body>
</html>
```